Ever Ready Path

Have clients check their mortgage qualifications before they go looking for a mortgage lender. This program gains access to your lenders credit report / 3 scores without impacting your credit scores.

```html
<!DOCTYPE html>
<html lang="en">
<head>
<meta charset="utf-8">
<title>Ever Ready Path – Business Card</title>
<link rel="stylesheet" href="https://fonts.googleapis.com/css2?family=Poppins:wght@500;600&family=Open+Sans:wght@400;600&family=Roboto+Condensed:wght@400;700&display=swap">
<style>
  :root {
    --backdrop: #3b3b3d;
    --blue: #1f4fc9;
    --blue-deep: #1a3fb0;
    --green: #22c07e;
    --green-soft: #2fcf8a;
    --white: #ffffff;
    --paper: #f6f6f4;
    --ink: #222222;
    --ink-soft: #3a3a3a;
  }
  * { margin: 0; padding: 0; box-sizing: border-box; }
  html, body { width: 1200px; height: 852px; overflow: hidden; }
  body {
    background: var(--backdrop);
    font-family: "Open Sans", Arial, sans-serif;
    position: relative;
  }
  .card {
    position: absolute;
    width: 540px;
    height: 310px;
    border-radius: 22px;
    overflow: hidden;
  }
  /* ---------- Front ---------- */
  .card-front { left: 40px; top: 271px; background: var(--blue); }
  .front-band {
    position: absolute; left: 0; top: 70px; width: 100%; height: 190px;
    background: var(--green);
  }
  .front-logo {
    position: absolute; left: 34px; top: 30px;
    display: flex; align-items: center; gap: 14px;
  }
  .logo-square {
    width: 40px; height: 40px; background: var(--white); border-radius: 4px;
  }
  .logo-name {
    font-family: "Poppins", Arial, sans-serif; font-weight: 600;
    font-size: 38px; color: var(--white); letter-spacing: -0.5px;
  }
  .front-tagline {
    position: absolute; left: 34px; top: 86px; right: 20px;
    font-size: 12px; color: var(--white);
  }
  .benefits {
    position: absolute; left: 34px; top: 118px; list-style: none;
    color: var(--ink); font-size: 14.5px; line-height: 1.35;
  }
  .benefits li { display: flex; gap: 10px; align-items: flex-start; margin-bottom: 4px; }
  .benefits svg { flex: none; margin-top: 3px; }
  .front-web {
    position: absolute; left: 0; right: 0; top: 272px; text-align: center;
    color: var(--white); font-size: 14px;
  }
  /* ---------- Back ---------- */
  .card-back { left: 620px; top: 271px; background: var(--paper); }
  .back-logo {
    position: absolute; left: 30px; top: 102px;
    display: flex; flex-direction: column; align-items: flex-start; gap: 12px;
  }
  .back-logo .logo-square { width: 70px; height: 56px; background: var(--blue); border-radius: 8px; margin-left: 40px; }
  .back-logo .logo-name { color: var(--blue); font-size: 30px; }
  .contact {
    position: absolute; left: 292px; top: 40px;
    font-family: "Roboto Condensed", Arial, sans-serif; color: var(--ink);
  }
  .contact-name { font-size: 24px; font-weight: 700; color: var(--blue); }
  .contact-role { font-size: 16px; margin-bottom: 12px; }
  .contact-lines { list-style: none; font-size: 15.5px; line-height: 1.3; }
  .contact-lines li { display: flex; gap: 10px; align-items: center; }
  .contact-address { font-size: 15.5px; line-height: 1.3; margin-top: 10px; padding-left: 22px; }
  .back-band {
    position: absolute; left: 0; bottom: 0; width: 100%; height: 40px;
    background: linear-gradient(90deg, var(--blue), var(--green));
    color: var(--white); font-family: "Roboto Condensed", Arial, sans-serif;
    font-size: 14px; display: flex; align-items: center; padding-left: 24px;
  }
  .back-band strong { font-weight: 700; margin-right: 4px; }
</style>
</head>
<body>

<section class="card card-front">
  <div class="front-band"></div>
  <div class="front-logo">
    <span class="logo-square"></span>
    <span class="logo-name">Ever Ready Path</span>
  </div>
  <p class="front-tagline">is Managed by Kinfolk Finance, A 401(c)(3) Nonprofit Certified Credit Counselor</p>
  <ul class="benefits">
    <li><svg width="14" height="14" viewBox="0 0 14 14"><rect width="14" height="14" fill="#fff"/><path d="M3 7.5l2.5 2.5L11 4" stroke="#1f4fc9" stroke-width="2" fill="none"/></svg>Discover Your Mortgage Qualifications - FHA, Conv., VA, USDA</li>
    <li><svg width="14" height="14" viewBox="0 0 14 14"><rect width="14" height="14" fill="#fff"/><path d="M3 7.5l2.5 2.5L11 4" stroke="#1f4fc9" stroke-width="2" fill="none"/></svg>Find Out Your Lender's 3 Credit (Classic) Scores</li>
    <li><svg width="14" height="14" viewBox="0 0 14 14"><rect width="14" height="14" fill="#fff"/><path d="M3 7.5l2.5 2.5L11 4" stroke="#1f4fc9" stroke-width="2" fill="none"/></svg>Your Credit Report will be Analyzed for Score Improvement</li>
    <li><svg width="14" height="14" viewBox="0 0 14 14"><rect width="14" height="14" fill="#fff"/><path d="M3 7.5l2.5 2.5L11 4" stroke="#1f4fc9" stroke-width="2" fill="none"/></svg><span>ERP will Identify Your Personal Steps to Higher Credit Scores<br>(66 Average Point Improvement)</span></li>
  </ul>
  <p class="front-web">www.EverReadyPath.org</p>
</section>

<section class="card card-back">
  <div class="back-logo">
    <span class="logo-square"></span>
    <span class="logo-name">Ever Ready Path</span>
  </div>
  <div class="contact">
    <p class="contact-name">Dana Morrow</p>
    <p class="contact-role">Managing Director</p>
    <ul class="contact-lines">
      <li><svg width="12" height="12" viewBox="0 0 12 12"><path d="M2 1h3l1 3-2 1a7 7 0 003 3l1-2 3 1v3c-6 0-9-3-9-9z" fill="#1f4fc9"/></svg>(800) 555-0142</li>
      <li><svg width="12" height="12" viewBox="0 0 12 12"><rect x="0.5" y="2" width="11" height="8" fill="#22c07e"/><path d="M1 2.5l5 4 5-4" stroke="#fff" fill="none"/></svg>Support@EverReadyPath.org</li>
      <li><svg width="12" height="12" viewBox="0 0 12 12"><circle cx="6" cy="6" r="5.2" fill="#1f4fc9"/><path d="M1 6h10M6 1v10M3 2.5q3 3.5 0 7M9 2.5q-3 3.5 0 7" stroke="#fff" stroke-width="0.8" fill="none"/></svg>www.EverReadyPath.org</li>
    </ul>
    <p class="contact-address">318 Harbor Lane, Suite 210,<br>Millbrook, Oregon 97001</p>
  </div>
  <div class="back-band"><strong>Ever Ready Path</strong> is Managed by Kinfolk Finance, A 401(c)(3) Nonprofit Certified Credit Counselor</div>
</section>

</body>
</html>
```